Business Cards for new orthopaedic surgery practice

My husband and I are starting our own orthopaedic surgery practice. We are looking for a business card that is uniform, but one will have my name/title and the other will have his. You can just create one design with my name on it for now. But when I choose your design as the winning design I will ask that you add another copy with his name/title.

We are looking for classy, simple, elite all in one. We like dark blues/a little gold/yellow. Something that goes with our logo. We want our logo incorporated. Here is all the info you need:
Business name: RV Spine & Vitality Center
Location: 38915 North Bramble Ave
Palm Hollow, FL 33490
Phone: 954-218-4630
Fax: 954-571-2846
Email: info@myrvspine.example

Names: Lucinda Ferrow, M.D.
Board Certified Hand and Upper Extremity Surgeon

Emeka Dlunga, M.D.
Board Certified Hip & Knee Replacement/General Orthopaedic Surgeon

Can decide what you want to put on the back. Maybe a slogan:
Rooted in Care. Focused on You

I am just going to upload our logo. The only thing is if we select you as the winning design, the location, and phone numbers may change. We will need your help to update that once fully solidified.

Industry/Entity Type

Medical

Contact Information for Business Card

Colors
0054AA
0677BA
7BADD7
CADEEF
E8F1F8
0094D4
00A9DD
6FCCEA
C7EBF8
E9F6FB

Requirements
Must have
• class, appeal,
Should not have
• We want to air on the side of masculine if we are looking at masculine vs. feminine feel. But we still want it classy, sophisticated, and something we will love

```html
<!DOCTYPE html>
<html lang="en">
<head>
<meta charset="utf-8">
<title>RV Spine &amp; Vitality Center – Business Card</title>
<link href="https://fonts.googleapis.com/css2?family=Montserrat:wght@500;600&display=swap" rel="stylesheet">
<style>
  :root {
    --backdrop: #e5e5e5;
    --navy: #1b2a50;
    --gold: #c6a15b;
    --paper: #ffffff;
  }
  * { margin: 0; padding: 0; box-sizing: border-box; }
  html, body { width: 1200px; height: 1200px; overflow: hidden; }
  body {
    background: var(--backdrop);
    font-family: "Montserrat", sans-serif;
    position: relative;
  }
  .card {
    position: absolute;
    left: 285px;
    width: 630px;
    height: 360px;
    overflow: hidden;
  }
  .card--front { top: 173px; background: var(--paper); }
  .card--back { top: 668px; background: var(--navy); }

  .brand {
    position: absolute;
    display: flex;
    flex-direction: column;
    align-items: center;
    text-align: center;
    font-weight: 600;
    letter-spacing: 0.14em;
    text-transform: uppercase;
  }
  .brand__dot {
    width: 14px; height: 14px; border-radius: 50%;
    margin-bottom: 12px;
    background: var(--gold);
  }
  .brand__name { font-size: 17px; line-height: 1.45; white-space: nowrap; }
  .card--front .brand { left: 50px; top: 108px; width: 240px; color: var(--navy); }
  .card--back .brand { left: 195px; top: 138px; width: 240px; color: var(--paper); }

  .contact {
    position: absolute;
    left: 376px;
    top: 104px;
    color: var(--navy);
    white-space: nowrap;
  }
  .contact__name { font-size: 20px; font-weight: 600; line-height: 1; }
  .contact__practice { font-size: 12px; font-weight: 500; margin-top: 7px; }
  .contact__list { list-style: none; margin-top: 10px; }
  .contact__item {
    display: flex; align-items: center;
    font-size: 12px; font-weight: 500; line-height: 14px;
    margin-bottom: 8px;
  }
  .contact__icon { width: 24px; height: 24px; flex: none; margin-right: 11px; }

  .card__bands { position: absolute; left: 0; top: 0; width: 630px; height: 360px; }
</style>
</head>
<body>
  <section class="card card--front">
    <div class="brand">
      <span class="brand__dot"></span>
      <span class="brand__name">RV Spine &amp;<br>Vitality Center</span>
    </div>

    <div class="contact">
      <h1 class="contact__name">Lucinda Ferrow, M.D.</h1>
      <p class="contact__practice">RV Spine &amp; Vitality Center</p>
      <ul class="contact__list">
        <li class="contact__item">
          <svg class="contact__icon" viewBox="0 0 24 24"><circle cx="12" cy="12" r="12" fill="#1b2a50"/><path d="M12 5.5a4 4 0 0 0-4 4c0 3 4 8 4 8s4-5 4-8a4 4 0 0 0-4-4z" fill="#fff"/><circle cx="12" cy="9.6" r="1.5" fill="#1b2a50"/></svg>
          <span>38915 North Bramble Ave<br>Palm Hollow, FL 33490</span>
        </li>
        <li class="contact__item">
          <svg class="contact__icon" viewBox="0 0 24 24"><circle cx="12" cy="12" r="12" fill="#1b2a50"/><path d="M8.6 6.5l1.8-.4 1.2 2.8-1.3 1c.6 1.4 1.6 2.4 3 3l1-1.3 2.8 1.2-.4 1.8c-.2.6-.8 1-1.5.9C11.1 15 9 12.9 7.6 8c-.1-.7.3-1.3 1-1.5z" fill="#fff"/></svg>
          <span>954-218-4630<br>954-571-2846</span>
        </li>
        <li class="contact__item">
          <svg class="contact__icon" viewBox="0 0 24 24"><circle cx="12" cy="12" r="12" fill="#1b2a50"/><rect x="6.5" y="8.3" width="11" height="7.4" fill="none" stroke="#fff" stroke-width="1"/><path d="M6.5 8.3l5.5 4.2 5.5-4.2M6.5 15.7l4-3.4M17.5 15.7l-4-3.4" fill="none" stroke="#fff" stroke-width="1"/></svg>
          <span>info@myrvspine.example</span>
        </li>
      </ul>
    </div>

    <svg class="card__bands" viewBox="0 0 630 360" aria-hidden="true">
      <polygon points="0,322 414,322 392,334 0,334" fill="#c6a15b"/>
      <polygon points="0,344 394,344 468,304 630,304 630,360 0,360" fill="#1b2a50"/>
    </svg>
  </section>

  <section class="card card--back">
    <div class="brand">
      <span class="brand__dot"></span>
      <span class="brand__name">RV Spine &amp;<br>Vitality Center</span>
    </div>
  </section>
</body>
</html>
```